Design a New Business Card for Our Company

We are looking for fresh, unique, and a modern business card that reflects our roots as digital marketing agency focused on SEM.

Industry/Entity Type

Marketing

Contact Information for Business Card

looking for very unique out of the box designs. clean and modern that compliments our logo

Requirements
Must have
• colors should match our logo
• Front should have name, address, email, and phone/fax of the person, phone/fax are the same number
• back should have our url

```html
<!DOCTYPE html>
<html lang="en">
<head>
<meta charset="utf-8">
<title>Brightway Solutions – Business Card</title>
<link rel="stylesheet" href="https://fonts.googleapis.com/css2?family=Open+Sans:wght@400;600&display=swap">
<style>
  :root {
    --page: #ecebe8;
    --card-grey: #a7a8aa;
    --card-white: #ffffff;
    --brand-blue: #4a8fd6;
    --brand-blue-soft: rgba(74, 143, 214, 0.55);
    --text-light: #ffffff;
    --shadow: rgba(0, 0, 0, 0.18);
  }
  * { box-sizing: border-box; margin: 0; padding: 0; }
  html, body {
    width: 1200px; height: 878px; overflow: hidden;
    background: var(--page);
    font-family: "Open Sans", Arial, sans-serif;
  }
  .canvas {
    width: 1200px; height: 878px;
    display: flex; align-items: center; justify-content: center; gap: 44px;
  }
  .card {
    position: relative;
    width: 540px; height: 309px;
    overflow: hidden;
    box-shadow: 0 10px 24px var(--shadow);
  }

  /* Front: personal details */
  .card-front { background: var(--card-grey); }
  .front-band {
    position: absolute; left: 0; right: 0; bottom: 0; height: 58px;
    background: var(--card-white);
    border-bottom: 4px solid var(--brand-blue);
  }
  .front-texture {
    position: absolute; left: 240px; top: 30px; width: 200px; height: 130px;
    background: radial-gradient(ellipse at center, rgba(255,255,255,0.4) 0%, rgba(255,255,255,0) 70%);
  }
  .front-pattern {
    position: absolute; right: 22px; bottom: 20px; width: 200px; height: 170px;
    border-radius: 50%;
    background:
      radial-gradient(ellipse at 35% 30%, rgba(255,255,255,0.85) 0%, rgba(255,255,255,0) 55%),
      radial-gradient(ellipse at 60% 75%, var(--brand-blue-soft) 0%, rgba(74,143,214,0) 60%);
  }
  .front-details {
    position: absolute; left: 36px; top: 28px;
    color: var(--text-light);
  }
  .holder-name { font-size: 30px; font-weight: 400; line-height: 1.1; }
  .holder-title { font-size: 13px; margin-top: 4px; }
  .contact-list { list-style: none; margin-top: 18px; font-size: 13px; line-height: 1.6; }
  .contact-list .label { display: inline-block; width: 18px; }
  .contact-list .gap { display: inline-block; width: 34px; }
  .address { margin-top: 14px; font-size: 13px; line-height: 1.5; }

  /* Back: brand and url */
  .card-back { background: var(--card-white); }
  .brand {
    position: absolute; left: 0; right: 0; top: 78px;
    display: flex; align-items: center; justify-content: center; gap: 14px;
  }
  .brand-dot { width: 26px; height: 26px; border-radius: 50%; background: var(--brand-blue); }
  .brand-name { font-size: 36px; font-weight: 600; color: var(--brand-blue); letter-spacing: 0.5px; }
  .back-band {
    position: absolute; left: 0; right: 0; bottom: 0; height: 88px;
    background: var(--card-grey);
    display: flex; align-items: center; padding-left: 32px;
  }
  .web-address { color: var(--text-light); font-size: 14px; letter-spacing: 0.5px; }
</style>
</head>
<body>
  <main class="canvas">
    <section class="card card-front" aria-label="Business card front">
      <div class="front-band"></div>
      <div class="front-texture" role="img" aria-label="Soft dotted texture behind the contact details"></div>
      <div class="front-pattern" role="img" aria-label="Decorative pattern of white and blue circles"></div>
      <div class="front-details">
        <h1 class="holder-name">Your Name</h1>
        <p class="holder-title">Job Title</p>
        <ul class="contact-list">
          <li><span class="label">P.</span>101 1010<span class="gap"></span><span class="label">F.</span>101 1010</li>
          <li><span class="label">E.</span>hello@brightwaysem.com</li>
        </ul>
        <p class="address">your adress, 9 your adres<br>PO Box 101, your adress</p>
      </div>
    </section>

    <section class="card card-back" aria-label="Business card back">
      <div class="brand">
        <span class="brand-dot"></span>
        <span class="brand-name">Brightway Solutions</span>
      </div>
      <div class="back-band">
        <span class="web-address">www.brightwaysem.com</span>
      </div>
    </section>
  </main>
</body>
</html>
```